Red Gum Business Card Design

We are a new small business specialising in under ground cable jointing and excavation works in NSW Australia.
Design I'm looking for is incorporating the Australian flag & excavator with out being to cheesy.
Maybe a faded washed out flag to help with overload of colour? & so its not the main focus.
Very open to creative out of the box designs!

Target Market(s)

Building & Construction

Industry/Entity Type

Construction

Contact Information for Business Card

Red Gum Cable Jointing & Excavations
Owen Falkirk

Ph: 0438 605 312
E: owen.falkirk@tallmail.example

Reverse Side
Services we offer:
High Voltage & Low Voltage Cable Jointing
Polymeric & paperlead jointing & terminations
Trenching & Auger Drilling 150 - 600mm
Site preparation / leveling / clearing
Driveway / Footpath / Turf Prep
Rubbish Removal
Tree & Stump removal
Footings & Post holes
Drainage
Service Installs
Gravels & Sands available
Any general Earth moving needs
Reliable Free Quotes
Fully Insured

Font styles to use
Serif
Script

Requirements
Nice to have
• small excavator (See uploaded picture)

```html
<!DOCTYPE html>
<html lang="en">
<head>
<meta charset="utf-8">
<title>Red Gum Business Card Design</title>
<link rel="stylesheet" href="https://fonts.googleapis.com/css2?family=Open+Sans:wght@400;700;800&family=Libre+Baskerville:wght@400&display=swap">
<style>
  :root {
    --backdrop: #e4e4e4;
    --card-blue: #0b8ad6;
    --card-charcoal: #2f2f31;
    --card-white: #ffffff;
    --ink-dark: #3a3a3c;
    --ink-light: #f2f2f2;
    --heading-ink: #111214;
  }
  * { box-sizing: border-box; }
  html, body {
    margin: 0;
    width: 1200px;
    height: 887px;
    overflow: hidden;
    background: var(--backdrop);
  }
  .sheet {
    position: relative;
    width: 1200px;
    height: 887px;
  }
  .card {
    position: absolute;
    top: 295px;
    width: 520px;
    height: 297px;
    overflow: hidden;
    box-shadow: 0 6px 18px rgba(0,0,0,0.18);
  }
  .card-back { left: 60px; background: var(--card-blue); }
  .card-front { left: 620px; background: var(--card-white); }
  .card-shapes {
    position: absolute;
    inset: 0;
    width: 100%;
    height: 100%;
  }

  /* Reverse side */
  .services-title {
    position: absolute;
    top: 30px;
    left: 150px;
    margin: 0;
    font-family: "Open Sans", sans-serif;
    font-weight: 800;
    font-size: 23px;
    letter-spacing: 0.2px;
    color: var(--heading-ink);
  }
  .services {
    position: absolute;
    top: 76px;
    left: 30px;
    display: flex;
    gap: 26px;
  }
  .services ul {
    margin: 0;
    padding: 0;
    list-style: none;
    font-family: "Open Sans", sans-serif;
    font-size: 11px;
    line-height: 16px;
    color: var(--ink-light);
  }
  .services li { position: relative; padding-left: 11px; white-space: nowrap; }
  .services li::before {
    content: "";
    position: absolute;
    left: 0;
    top: 6px;
    width: 4px;
    height: 4px;
    border-radius: 50%;
    background: var(--heading-ink);
  }

  /* Front side */
  .holder-name {
    position: absolute;
    top: 28px;
    right: 40px;
    margin: 0;
    font-family: "Libre Baskerville", serif;
    font-weight: 400;
    font-size: 24px;
    color: var(--ink-light);
  }
  .contact {
    position: absolute;
    top: 80px;
    left: 40px;
    margin: 0;
    padding: 0;
    list-style: none;
    font-family: "Open Sans", sans-serif;
    font-size: 12px;
    line-height: 24px;
    color: var(--ink-light);
  }
  .contact li { display: flex; align-items: center; gap: 10px; }
  .contact svg { width: 12px; height: 12px; fill: var(--ink-light); }
  .company {
    position: absolute;
    top: 188px;
    right: 48px;
    display: flex;
    align-items: center;
    gap: 12px;
  }
  .company-mark {
    width: 14px;
    height: 14px;
    background: var(--card-blue);
  }
  .company-name {
    margin: 0;
    font-family: "Libre Baskerville", serif;
    font-weight: 400;
    font-size: 19px;
    line-height: 26px;
    color: var(--ink-dark);
  }
</style>
</head>
<body>
<main class="sheet">

  <section class="card card-back" aria-label="Reverse side: services">
    <svg class="card-shapes" viewBox="0 0 520 297" aria-hidden="true">
      <polygon points="0,182 520,250 520,268 468,297 0,297" fill="var(--card-charcoal)"/>
    </svg>
    <h2 class="services-title">SERVICES WE OFFER:</h2>
    <div class="services">
      <ul>
        <li>High Voltage &amp; Low Voltage Cable Jointing</li>
        <li>Polymeric &amp; paperlead jointing &amp; terminations</li>
        <li>Trenching &amp; Auger Drilling 150 - 600mm</li>
        <li>Site preparation / leveling / clearing</li>
        <li>Driveway / Footpath / Turf Prep</li>
        <li>Rubbish Removal</li>
        <li>Tree &amp; Stump removal</li>
      </ul>
      <ul>
        <li>Footings &amp; Post holes</li>
        <li>Drainage</li>
        <li>Service Installs</li>
        <li>Gravels &amp; Sands available</li>
        <li>Any general Earth moving needs</li>
        <li>Reliable Free Quotes</li>
        <li>Fully Insured</li>
      </ul>
    </div>
  </section>

  <section class="card card-front" aria-label="Front side: contact">
    <svg class="card-shapes" viewBox="0 0 520 297" aria-hidden="true">
      <polygon points="0,0 520,0 520,146 0,158" fill="var(--card-charcoal)"/>
      <polygon points="0,0 96,0 0,34" fill="var(--card-blue)"/>
      <polygon points="0,152 78,156 0,176" fill="var(--card-blue)"/>
      <polygon points="520,138 520,160 470,150" fill="var(--card-blue)"/>
      <polygon points="520,246 520,264 430,297 400,297" fill="var(--card-blue)"/>
      <polygon points="520,262 520,297 430,297" fill="var(--card-charcoal)"/>
    </svg>
    <h1 class="holder-name">Owen Falkirk</h1>
    <ul class="contact">
      <li>
        <svg viewBox="0 0 12 12" aria-hidden="true"><path d="M2.5 0.8l2 2.2-1.1 1.4c0.8 1.6 2 2.8 3.6 3.6l1.4-1.1 2.2 2-1.2 2C5 10.5 1.5 7 0.5 2z"/></svg>
        <span>0438 605 312</span>
      </li>
      <li>
        <svg viewBox="0 0 12 12" aria-hidden="true"><path d="M0.5 2h11v8h-11zM1.5 3l4.5 3.5L10.5 3v-0.2h-9z" fill-rule="evenodd"/></svg>
        <span>owen.falkirk@tallmail.example</span>
      </li>
    </ul>
    <div class="company">
      <span class="company-mark" aria-hidden="true"></span>
      <p class="company-name">Red Gum Cable Jointing<br>&amp; Excavations</p>
    </div>
  </section>

</main>
</body>
</html>
```